Print & digital package needed for technology firm

We need a package of coordinating marketing materials for our technology business. We offer technology solutions to midsized organizations, including data center, outsourced IT, and technology consulting. Find more information on our website, www.pexlora.com. Design is the main concern, we can modify the text ongoing to best reflect our company’s offerings. The design should communicate technology expertise and strategic thinking. Our website is currently being updated with a “flat design” theme and we’d like design of these items to be flat, fresh, modern, and professional, without being boring.
Please use attached logo - can send in .ai/.eps/.psd/etc. Fonts in logo are Futura, Futura Book, and Lato. Please use pexLORA blue, #0372bb.
Please find attached one of our product flyers for one of the computers we lease. Fonts used are Roboto Slab (partial to this font) & Lato. Also attached copy of our business card design.
Taglines we have used include “Does IT hear what troubles you?” and “IT made simple” although we are open to new ideas.
Would like final products to be available in editable files - .psd/.tif/.ai/etc.

- 1 PowerPoint template
- 1 leaderboard ad (digital, 72dpi)
- 1 medium rectangle ad 300x250 (digital, 72dpi)
- 1 full page ad 8x11 (print, 300dpi)
- 1 half-page ad horizontal (print, 300dpi)
- 1 letterhead template
- 1 proposal front-page

There is potential for further graphic/print design opportunities for our business as well.

All, thank you for your assistance in understanding the budget process with this type of design contest - we have updated the project's budget to reflect the items we are requesting.

Please email mvarga at pexlora.com with inquiries or comments. Thank you.

Designers,

Due to an oversight, our project was listed as "refundable" - this has been corrected and changed to committed payment.
To enter into this contest, please pick 2-3 items from the list of desired materials (ads, powerpoint, letterhead, etc.) It is not necessary to submit all items which will be part of the final package to be considered for the contest.

Thank you. Please contact mvarga@pexlora.com for questions.
Best,
Mimi

CEOs, CFOs, CIOs, COOs - college+ educated, 30-60, professional.

```html
<!DOCTYPE html>
<html lang="en">
<head>
<meta charset="utf-8">
<title>pexLORA – Infographic Ad</title>
<link rel="stylesheet" href="https://fonts.googleapis.com/css2?family=Open+Sans:ital,wght@0,300;0,400;0,600;0,700;1,300;1,700&family=PT+Sans:wght@400&display=swap">
<style>
  :root {
    --brand-blue: #0372bb;
    --panel-blue: #1470ba;
    --sky-blue: #1ea6ea;
    --icon-blue: #1467b3;
    --ink: #2a2a2a;
    --muted: #555555;
    --white: #ffffff;
    --photo-dark: #1b1d20;
    --photo-mid: #34373b;
  }
  * { margin: 0; padding: 0; box-sizing: border-box; }
  html, body { width: 1200px; height: 1000px; overflow: hidden; background: var(--white); }
  body { font-family: "Open Sans", Arial, sans-serif; position: relative; }

  .ad { position: relative; width: 1200px; height: 1000px; overflow: hidden; background: var(--white); }

  .icon-bar { position: absolute; top: 0; left: 0; width: 1200px; height: 130px; }
  .icon-bar svg { position: absolute; top: 46px; width: 48px; height: 48px; }

  .hero-photo {
    position: absolute; top: 130px; left: 0; width: 1200px; height: 723px;
    background:
      linear-gradient(90deg, rgba(0,0,0,.35) 0%, rgba(0,0,0,0) 40%, rgba(0,0,0,.2) 100%),
      linear-gradient(180deg, var(--photo-mid) 0%, var(--photo-dark) 55%, #222427 100%);
  }

  .headline {
    position: absolute; left: 62px; top: 204px;
    font-size: 151px; font-weight: 400; line-height: 1; letter-spacing: 0;
    color: var(--sky-blue);
  }
  .subline {
    position: absolute; right: 82px; top: 348px;
    font-size: 45px; font-weight: 300; line-height: 1; color: var(--white);
    letter-spacing: 0.3px;
  }

  .speaker-card {
    position: absolute; left: 0; top: 393px; width: 341px; height: 218px;
    background: var(--white); border-radius: 0 46px 0 46px;
  }
  .speaker-card svg { position: absolute; left: 98px; top: 38px; }

  .side-tab {
    position: absolute; left: 1120px; top: 488px; width: 80px; height: 124px;
    background: var(--panel-blue); border-radius: 46px 0 0 0;
  }

  .message-panel {
    position: absolute; left: 342px; top: 612px; width: 808px; height: 176px;
    background: var(--panel-blue); border-radius: 0 0 26px 26px; color: var(--white);
  }
  .message-title {
    position: absolute; left: 62px; top: 14px;
    font-size: 43px; font-style: italic; font-weight: 300; line-height: 1.1; white-space: nowrap;
  }
  .message-title strong { font-weight: 700; }
  .message-body {
    position: absolute; left: 59px; top: 82px; width: 650px; height: 76px;
    column-count: 2; column-gap: 46px; column-fill: balance;
    font-family: "PT Sans", Arial, sans-serif;
    font-size: 11.4px; line-height: 15px; text-align: justify;
  }

  .footer { position: absolute; left: 0; top: 853px; width: 1200px; height: 147px; }
  .slogan, .follow { position: absolute; top: 61px; font-size: 17px; font-weight: 300; color: var(--muted); }
  .slogan { left: 52px; }
  .divider { position: absolute; left: 199px; top: 57px; width: 6px; height: 33px; border-left: 1px solid #888; border-right: 1px solid #888; }
  .follow { left: 230px; }
  .social-list { position: absolute; left: 343px; top: 62px; display: flex; gap: 14px; list-style: none; }
  .social-list li { display: flex; align-items: center; gap: 5px; font-size: 12px; font-weight: 600; color: var(--muted); }
  .social-list li::before { content: ""; width: 14px; height: 14px; background: var(--brand-blue); border-radius: 2px; }

  .brand {
    position: absolute; right: 103px; top: 40px;
    font-size: 44px; font-weight: 600; line-height: 1; color: var(--ink);
    text-transform: uppercase; letter-spacing: 3px;
  }
  .brand-services { position: absolute; right: 76px; top: 92px; font-size: 14px; color: var(--muted); word-spacing: 2px; }
</style>
</head>
<body>
<main class="ad">

  <div class="icon-bar" aria-hidden="true">
    <svg style="left:68px" viewBox="0 0 48 48" fill="none" stroke="var(--icon-blue)" stroke-width="3"><circle cx="24" cy="24" r="21.5"/><rect x="14" y="17" width="20" height="14" stroke-width="2.2"/><path d="M14 17l10 8 10-8" stroke-width="2.2"/></svg>
    <svg style="left:182px" viewBox="0 0 48 48" fill="none" stroke="var(--icon-blue)" stroke-width="3"><circle cx="24" cy="24" r="21.5"/><path d="M14 19h5l2-3h6l2 3h5v12H14z" fill="var(--icon-blue)" stroke="none"/><circle cx="24" cy="25" r="3.6" fill="#fff" stroke="none"/></svg>
    <svg style="left:297px" viewBox="0 0 48 48" fill="none" stroke="var(--icon-blue)" stroke-width="3"><circle cx="24" cy="24" r="21.5"/><circle cx="27" cy="21" r="6" stroke-width="2.6"/><path d="M22.5 25.5L15 33" stroke-width="3.4" stroke-linecap="round"/></svg>
    <svg style="left:412px" viewBox="0 0 48 48" fill="none" stroke="var(--icon-blue)" stroke-width="3"><circle cx="24" cy="24" r="21.5"/><g fill="var(--icon-blue)" stroke="none"><circle cx="19" cy="18" r="3"/><circle cx="26" cy="18" r="3"/><rect x="14" y="21" width="16" height="10" rx="1"/><path d="M30 24l5-3v10l-5-3z"/></g></svg>
    <svg style="left:527px" viewBox="0 0 48 48" fill="none" stroke="var(--icon-blue)" stroke-width="3"><circle cx="24" cy="24" r="21.5"/><circle cx="24" cy="24" r="9" stroke-width="2.2"/><path d="M24 18v6h4" stroke-width="2.2"/></svg>
    <svg style="left:642px" viewBox="0 0 48 48" fill="none" stroke="var(--icon-blue)" stroke-width="3"><circle cx="24" cy="24" r="21.5"/><circle cx="24" cy="15" r="2.4" fill="var(--icon-blue)" stroke="none"/><rect x="22" y="20" width="4" height="15" fill="var(--icon-blue)" stroke="none"/></svg>
    <svg style="left:757px" viewBox="0 0 48 48" fill="none" stroke="var(--icon-blue)" stroke-width="3"><circle cx="24" cy="24" r="21.5"/><rect x="17" y="13" width="14" height="22" rx="1.5" stroke-width="2"/><rect x="19.5" y="16" width="9" height="4" fill="var(--icon-blue)" stroke="none"/><g fill="var(--icon-blue)" stroke="none"><rect x="19.5" y="22.5" width="2.4" height="2.4"/><rect x="22.8" y="22.5" width="2.4" height="2.4"/><rect x="26.1" y="22.5" width="2.4" height="2.4"/><rect x="19.5" y="26" width="2.4" height="2.4"/><rect x="22.8" y="26" width="2.4" height="2.4"/><rect x="26.1" y="26" width="2.4" height="2.4"/><rect x="19.5" y="29.5" width="2.4" height="2.4"/><rect x="22.8" y="29.5" width="2.4" height="2.4"/><rect x="26.1" y="29.5" width="2.4" height="2.4"/></g></svg>
    <svg style="left:873px" viewBox="0 0 48 48" fill="none" stroke="var(--icon-blue)" stroke-width="3"><circle cx="24" cy="24" r="21.5"/><path d="M30 13l5 5-14 14-6 1 1-6z" fill="var(--icon-blue)" stroke="none"/></svg>
    <svg style="left:988px" viewBox="0 0 48 48" fill="none" stroke="var(--icon-blue)" stroke-width="3"><circle cx="24" cy="24" r="21.5"/><rect x="14" y="15" width="20" height="19" stroke-width="2"/><rect x="14" y="15" width="20" height="5" fill="var(--icon-blue)" stroke="none"/><text x="24" y="31.5" text-anchor="middle" font-family="Open Sans, Arial, sans-serif" font-size="9" font-weight="700" fill="var(--icon-blue)" stroke="none">25</text></svg>
    <svg style="left:1103px" viewBox="0 0 48 48" fill="none" stroke="var(--icon-blue)" stroke-width="3"><circle cx="24" cy="24" r="21.5"/><circle cx="24" cy="26" r="8" stroke-width="2.2"/><path d="M24 22v4h3" stroke-width="2"/><path d="M15 17l4-3M33 17l-4-3" stroke-width="2.4" stroke-linecap="round"/></svg>
  </div>

  <div class="hero-photo" role="img" aria-label="Dark monochrome photograph of server racks in a data center aisle"></div>

  <h1 class="headline">INFOGRAPHIC</h1>
  <p class="subline">based ad for digital and social media</p>

  <div class="speaker-card">
    <svg width="150" height="140" viewBox="0 0 150 140" aria-hidden="true">
      <path d="M2 45h36L83 2v136L38 95H2z" fill="var(--icon-blue)"/>
      <path d="M100 48a30 30 0 0 1 0 44" fill="none" stroke="var(--icon-blue)" stroke-width="8"/>
      <path d="M114 25a58 58 0 0 1 0 90" fill="none" stroke="var(--icon-blue)" stroke-width="8"/>
    </svg>
  </div>

  <div class="side-tab" aria-hidden="true"></div>

  <section class="message-panel">
    <h2 class="message-title">Does <strong>IT</strong> hear what troubles you?</h2>
    <p class="message-body">Quisque interdum nunc non velit euismod sit amet dictum diam lacinia. Vestibulum est lacus, ultricies a scelerisque et, accumsan ut quam. Aliquam id sapien sed urna tempus hendrerit. Curabitur lobortis justo sed risus consectetur dapibus. Mauris molestie velit ut turpis sodales viverra. Nam eu libero diam, a rutrum dolor. Aenean ac placerat ante. Morbi ac felis justo, eu vehicula justo. Nulla dapibus, felis ac pretium lacinia, lacus libero scelerisque nisi, porttitor tincidunt mauris eget odio. In iaculis elit at enim semper bibendum. Curabitur porttitor eros ut tortor</p>
  </section>

  <footer class="footer">
    <p class="slogan">IT made simple!</p>
    <span class="divider" aria-hidden="true"></span>
    <p class="follow">Follow us on</p>
    <ul class="social-list">
      <li>Linkfold</li>
      <li>Chirpwave</li>
      <li>Crowdnest</li>
    </ul>
    <p class="brand">pexLORA</p>
    <p class="brand-services">IT Consulting | Managed Services | Data Center</p>
  </footer>

</main>
</body>
</html>
```